Business Card Design Project

I need a business card design for our new logo, please check the logo at the following link:
https://www.filecrate.net/s/q7rtx2pw9kd41m/FernLoop.png
The address on the business card:
Av. Gervásio Tavares 418 sala 207
Barra da Tijuca, Rio de Janeiro, RJ
CEP: 22714-380
Brasil
Phone: +55 21 86347215
e-mail: osvaldo@fernloop.com.br
Updates
Thank you all for sending your designs, we will not provide feedback because there are too many designs, on December 3 we will pick the best design according to our point of view. Please keep posting.
Osvaldo
Industry/Entity Type
Business
Look and feel
Each slider illustrates characteristics of the customer's brand and the style your logo design should communicate.

```html
<!DOCTYPE html>
<html lang="pt-BR">
<head>
<meta charset="UTF-8">
<title>FernLoop – Business Card</title>
<link rel="stylesheet" href="https://fonts.googleapis.com/css2?family=Nunito+Sans:wght@400;700;800&display=swap">
<style>
  :root {
    --backdrop: #2e2e2e;
    --card: #ffffff;
    --ink: #1f1f1f;
    --accent: #f5c400;
    --art-dark: #222222;
    --art-mid: #3a3a3a;
  }
  * { margin: 0; padding: 0; box-sizing: border-box; }
  html, body {
    width: 1200px;
    height: 900px;
    overflow: hidden;
    background: var(--backdrop);
    font-family: "Nunito Sans", Arial, sans-serif;
    color: var(--ink);
  }
  .canvas { position: relative; width: 1200px; height: 900px; }
  .card {
    position: absolute;
    top: 308px;
    width: 513px;
    height: 284px;
    background: var(--card);
    border-radius: 28px;
    overflow: hidden;
  }
  .card--front { left: 73px; }
  .card--back { left: 615px; }

  .illustration {
    position: absolute;
    background: linear-gradient(135deg, var(--art-mid), var(--art-dark) 70%, var(--accent));
  }
  .illustration--emblem {
    left: 165px; top: 80px; width: 176px; height: 90px;
    border-radius: 40px 40px 30px 30px;
  }
  .illustration--runner-left {
    left: -20px; top: 60px; width: 145px; height: 148px;
    border-radius: 0 70px 60px 0;
  }
  .illustration--runner-right {
    left: 398px; top: 62px; width: 140px; height: 160px;
    border-radius: 70px 0 0 60px;
    background: linear-gradient(225deg, var(--art-mid), var(--art-dark) 70%, var(--accent));
  }

  .brand-name {
    position: absolute;
    left: 0; width: 100%;
    text-align: center;
    font-weight: 800;
    color: var(--ink);
    letter-spacing: -0.5px;
    line-height: 1;
  }
  .card--front .brand-name { top: 185px; font-size: 46px; }
  .card--back .brand-name { top: 34px; font-size: 58px; left: -6px; }

  .website {
    position: absolute;
    top: 259px; left: 0; width: 100%;
    text-align: center;
    font-size: 11px;
  }

  .contact {
    position: absolute;
    top: 124px; left: 0; width: 100%;
    text-align: center;
    font-size: 11px;
    line-height: 13.6px;
  }
  .contact__name { font-size: 18px; font-weight: 700; line-height: 22px; }
  .contact__role { font-size: 12.5px; font-weight: 700; line-height: 16px; margin-bottom: 12px; }
  .contact__address { margin-bottom: 14px; }
</style>
</head>
<body>
<div class="canvas">
  <section class="card card--front">
    <div class="illustration illustration--emblem" role="img" aria-label="Brand illustration of a running character with hat and briefcase"></div>
    <div class="brand-name">FernLoop</div>
    <div class="website">www.fernloop.com.br</div>
  </section>

  <section class="card card--back">
    <div class="illustration illustration--runner-left" role="img" aria-label="Cropped brand character illustration running in from the left edge"></div>
    <div class="illustration illustration--runner-right" role="img" aria-label="Cropped brand character illustration carrying a briefcase at the right edge"></div>
    <div class="brand-name">FernLoop</div>
    <div class="contact">
      <p class="contact__name">Osvaldo Ferraz</p>
      <p class="contact__role">founder and owner</p>
      <p class="contact__address">
        Av. Gervásio Tavares 418 sala 207<br>
        Barra da Tijuca, Rio de Janeiro, RJ<br>
        CEP: 22714-380<br>
        Brasil
      </p>
      <p class="contact__lines">
        +55 21 86347215<br>
        osvaldo@fernloop.com.br
      </p>
    </div>
  </section>
</div>
</body>
</html>
```